Luxury Wine Label for New Startup Winery

We need a wine label for our new winery startup. We have worked with a local designer but do not feel the resulting label / logo have the elevation required to present our brand as a luxury wine. Our winery is called "Harrowgate Vineyards" and we are focused on extremely high quality hand crafted artisan and estate wines from the Pacific Northwest.
We would like to see designs that utilize a tree line, or other imagery that represents the "Harrowgate" part of our company name. Another interesting feature could be wood grain.
A logo will be required based on your design so please design with this in mind:
This logo should be consistent with the wine bottle label design, and should be representative of our high end exclusive wine while giving a sense of place (Oregon/ Pacific Northwest.)
I will supply an image of the design we received from our local designer, PLEASE NOTE: in general we do like wood grain and tree line concepts but feel the execution was poorly done.
ATTN: Logo design should be suitable for use on: Bottles (Red wine/rose/white wine), Bussiness cards, vehicle signage, business signage, etc
P.S.:
If you have a design that is not outside the box we are still interested in seeing it.
Label is for a burgundy style bottle with a label height of 3.5 - 4" and a width of 3.5-4"
any label <= 4"x4" and >=3.5"x3.5" will be acceptable:
HOWEVER Width should be greater than or equal to height due to the bottle format
Target Market(s)
Wine enthusiasts with adequate discretionary budgets to afford $100 bottles of wine.
Industry/Entity Type
Wine / Winery
Requirements
Must have
- A sense of luxury, a feel of exclusivity, and a theme consistent with our product and brand name
Nice to have
- Tree line, wood grain or other wood themes. Serif fonts
Should not have
- anything cheesy, off topic, hard to read script fonts or anything that makes the label hard to read from a few feet away or too busy

```html
<!DOCTYPE html>
<html lang="en">
<head>
<meta charset="utf-8">
<title>Harrowgate Vineyards — Syrah Label</title>
<link href="https://fonts.googleapis.com/css2?family=Cinzel:wght@400;500;600&family=Pinyon+Script&family=Cormorant+Garamond:wght@500&display=swap" rel="stylesheet">
<style>
  :root {
    --page: #edf0f1;
    --label-black: #000000;
    --rule-olive: #6f6a50;
    --gold-deep: #d1ba5a;
    --gold-light: #f3ead6;
    --wood-mid: #763a22;
    --wood-dark: #331a14;
    --tan: #d7aa78;
    --tan-muted: #a9734c;
  }
  html, body {
    margin: 0;
    width: 1200px;
    height: 1200px;
    overflow: hidden;
    background: var(--page);
  }
  .canvas { display: block; width: 1200px; height: 1200px; }
  .brand-line { font-family: 'Cinzel', serif; font-weight: 500; }
  .region-line { font-family: 'Cinzel', serif; font-weight: 500; }
  .varietal { font-family: 'Pinyon Script', cursive; }
  .vintage-line { font-family: 'Cormorant Garamond', serif; font-weight: 500; }
</style>
</head>
<body>
<svg class="canvas" viewBox="0 0 1200 1200" xmlns="http://www.w3.org/2000/svg">
  <defs>
    <linearGradient id="gold-sheen" x1="0" y1="0" x2="1" y2="0">
      <stop offset="0" stop-color="var(--gold-deep)"/>
      <stop offset="0.5" stop-color="var(--gold-light)"/>
      <stop offset="1" stop-color="var(--gold-deep)"/>
    </linearGradient>
    <linearGradient id="wood-tone" x1="0" y1="0" x2="0" y2="1">
      <stop offset="0" stop-color="var(--wood-dark)"/>
      <stop offset="0.15" stop-color="var(--wood-mid)"/>
      <stop offset="0.45" stop-color="#5a2c1b"/>
      <stop offset="0.7" stop-color="var(--wood-mid)"/>
      <stop offset="1" stop-color="#4a2418"/>
    </linearGradient>
  </defs>

  <!-- Main label -->
  <g class="main-label">
    <rect x="299" y="320" width="602" height="401" fill="var(--label-black)"/>
    <rect class="rule" x="316" y="352" width="566" height="5" fill="var(--rule-olive)"/>
    <rect class="treeline" x="316" y="366" width="566" height="126" fill="url(#gold-sheen)"
          role="img" aria-label="Gold silhouette of an evergreen tree line"/>
    <text class="brand-line" x="600" y="556" font-size="44" text-anchor="middle"
          textLength="396" lengthAdjust="spacingAndGlyphs" fill="url(#gold-sheen)">HARROWGATE</text>
    <text class="brand-line" x="600" y="610" font-size="44" text-anchor="middle"
          textLength="386" lengthAdjust="spacingAndGlyphs" fill="url(#gold-sheen)">VINEYARDS</text>
    <text class="region-line" x="600" y="659" font-size="27" text-anchor="middle"
          textLength="384" lengthAdjust="spacingAndGlyphs" fill="url(#gold-sheen)">WILIAMETTE VALLEY</text>
    <rect class="rule" x="316" y="688" width="566" height="5" fill="var(--rule-olive)"/>
  </g>

  <!-- Varietal strip -->
  <g class="varietal-strip">
    <rect x="300" y="739" width="600" height="142" fill="url(#wood-tone)"
          role="img" aria-label="Dark walnut wood grain texture"/>
    <rect x="317" y="750" width="566" height="5" fill="var(--tan)"/>
    <text class="varietal" x="600" y="825" font-size="86" text-anchor="middle" fill="var(--tan)">Syrah</text>
    <rect x="317" y="862" width="107" height="5" fill="var(--tan)"/>
    <rect x="776" y="862" width="107" height="5" fill="var(--tan)"/>
    <text class="vintage-line" x="600" y="871" font-size="23" text-anchor="middle"
          textLength="290" lengthAdjust="spacingAndGlyphs" fill="var(--tan-muted)">ESTATE | 2023 | GROWN</text>
  </g>
</svg>
</body>
</html>
```